Consulting Firm stationery design

Now that the ArtHive has given us a new logo we'll now need to have all our stationery designed. So we're asking for this community to help us once again.We're looking to get from you Letterheads (Header and Footer, suitable to be applied on a .docx format. Vectors are required but keep this in mind), Envelopes (Front and Back designs, back is not a must but desirable depending on your design), 9"x 12" Pocket Folders (consider design for front and back, also for pockets as well), Business Cards.An elegant design is a must have, mostly for Folders and Envelopes. The idea with this two is to stand out from others when they're handed over. Ideas are welcomed, we were thinking maybe on some texturing simulation for these.Folders will have 3 addresses and contact information. Envelopes will have 1 address and contact information.Brand Manual attached. marquesino logo has been copyrighted already. I'm also attaching the current stationary designs (these never got to be out for production but was going to be before we made the brand changes); Pocker folders page 1 to 4 (pages 2 and 4 are the pocket designs), Pages 5 and 6 (6 is the back of the envelope), Pages 7 and 8 (8 is the back of the business card). No letterhead within these designs as it just had the logo and address.

Industry/Entity Type

Business Consultant

Font styles to use
Serif
Sans Serif

Requirements
Must have
• Elegance
Nice to have
• Modern looking out of common

```html
<!DOCTYPE html>
<html lang="en">
<head>
<meta charset="utf-8">
<title>marquesino — Pocket Folder Inside Spread</title>
<link href="https://fonts.googleapis.com/css2?family=Montserrat:wght@400;600;700&display=swap" rel="stylesheet">
<style>
  :root {
    --backdrop: #a6a6a6;
    --brand-blue: #0a7cba;
    --ink: #2b2b2b;
    --ink-soft: #5a5a5a;
    --white: #ffffff;
  }
  * { margin: 0; padding: 0; box-sizing: border-box; }
  html, body {
    width: 1200px; height: 1200px; overflow: hidden;
    background: var(--backdrop);
    font-family: "Montserrat", sans-serif;
  }
  .canvas { position: relative; width: 1200px; height: 1200px; }
  .folder-spread {
    position: absolute; left: 50px; top: 234px;
    width: 1100px; height: 733px;
  }
  .folder-spread svg { position: absolute; inset: 0; }
  .pocket-wordmark {
    position: absolute; left: 150px; top: 560px;
    color: var(--white); font-weight: 600; font-size: 58px;
    letter-spacing: -1px; white-space: nowrap;
  }
  .business-card {
    position: absolute; left: 796px; top: 690px;
    width: 262px; height: 150px;
    background: var(--white);
    color: var(--ink);
    font-size: 5.4px; line-height: 1.35;
  }
  .card-slot {
    position: absolute; width: 30px; height: 2px;
    background: var(--white); transform: rotate(-40deg);
  }
  .card-slot.top { left: 782px; top: 696px; }
  .card-slot.bottom { left: 1042px; top: 832px; }
  .card-brand {
    position: absolute; right: 14px; top: 12px;
    font-weight: 600; font-size: 14px; color: var(--ink);
    display: flex; align-items: center; gap: 4px;
  }
  .card-brand .dot { width: 6px; height: 6px; border-radius: 50%; background: var(--brand-blue); }
  .card-columns {
    position: absolute; left: 12px; right: 12px; top: 42px;
    display: flex; justify-content: space-between; gap: 10px;
  }
  .card-contact { width: 140px; }
  .card-office { width: 96px; white-space: nowrap; padding-top: 8px; }
  .card-name { font-size: 7px; font-weight: 700; white-space: nowrap; }
  .card-name span { font-weight: 400; }
  .card-creds { color: var(--ink-soft); margin-bottom: 6px; }
  .card-tagline { color: var(--brand-blue); font-weight: 600; font-size: 6px; margin-top: 6px; white-space: nowrap; }
  .card-legal { color: var(--ink-soft); margin-top: 5px; white-space: nowrap; }
  .card-office strong, .card-contact strong { font-weight: 700; }
  .card-phone { margin-top: 6px; }
  .card-web { margin-top: 6px; }
</style>
</head>
<body>
<main class="canvas">
  <section class="folder-spread" aria-label="Pocket folder inside spread">
    <svg width="1100" height="733" viewBox="0 0 1100 733">
      <defs>
        <linearGradient id="leftPanel" x1="0" x2="1" y1="0" y2="0">
          <stop offset="0" stop-color="#f4f4f4"/>
          <stop offset="1" stop-color="#dcdcdc"/>
        </linearGradient>
        <linearGradient id="rightPanel" x1="0" x2="1" y1="0" y2="0">
          <stop offset="0" stop-color="#dedede"/>
          <stop offset="1" stop-color="#f2f2f2"/>
        </linearGradient>
      </defs>
      <rect class="panel-left" x="0" y="0" width="550" height="733" fill="url(#leftPanel)"/>
      <rect class="panel-right" x="550" y="0" width="550" height="733" fill="url(#rightPanel)"/>
      <line class="spine-fold" x1="550" y1="0" x2="550" y2="733" stroke="#c9c9c9" stroke-width="1"/>
      <path class="pocket-left" d="M0 490 L470 448 Q492 446 500 466 L540 733 L0 733 Z" fill="var(--brand-blue)"/>
      <path class="pocket-right" d="M560 470 Q560 450 580 450 L1100 410 L1100 733 L570 733 Z" fill="var(--brand-blue)"/>
    </svg>
    <div class="pocket-wordmark">marquesino</div>
  </section>

  <span class="card-slot top"></span>
  <article class="business-card">
    <div class="card-brand">marquesino<span class="dot"></span></div>
    <div class="card-columns">
      <div class="card-contact">
        <p class="card-name">Rolan M. Vidal <span>| COO &amp; Partner</span></p>
        <p class="card-creds">ITC, MSMIT, ERP Certified, CISA, Predictive Analytics</p>
        <p><strong>D</strong> (555) 010 4420 ext. 201</p>
        <p><strong>M</strong> (555) 010 7731</p>
        <p><strong>E</strong> rolan@marquesino.example</p>
        <p class="card-tagline">Consultancy • Audit • Analytics</p>
        <p class="card-legal">MARQUESINO SRL<br>DR member firm of marquesino LLC</p>
      </div>
      <div class="card-office">
        <p><strong>MARQUESINO SRL</strong></p>
        <p>Alameda Business Tower</p>
        <p>Calle Ficticia 42, Centro</p>
        <p>Ciudad Modelo, Rep. Ficticia</p>
        <p class="card-phone"><strong>T</strong> (555) 010 4420</p>
        <p><strong>E</strong> info@marquesino.example</p>
        <p class="card-web">www.marquesino.example</p>
      </div>
    </div>
  </article>
  <span class="card-slot bottom"></span>
</main>
</body>
</html>
```